Larkspur Realty

Business cards for 4 people

They need to say for all
57 Danner Quay, Boston MA 02117

Each person will have their own personal information
We would like gold embossing for the name of the company
Mabel is the blonde sitting in the chair smiling her information should be on the back of the card with her name and information
Should say for slogan classic pattern, elevated experience
mabel@larkspurhomesnet.com
(413) 555-0182

Odessa is the brunette with wavy hair in the tan suit odessa@larkspurhomesnet.com
(617) 555-0147

june@larkspurhomesnet.com
(413) 555-0169
standing next to the chair

ruth@larkspurhomesnet.com
(413) 555-0193
close up headshot

```html
<!DOCTYPE html>
<html lang="en">
<head>
<meta charset="utf-8">
<title>Larkspur Realty – Business Cards</title>
<link rel="stylesheet" href="https://fonts.googleapis.com/css2?family=Montserrat:wght@400;500;700;800&display=swap">
<style>
  :root {
    --backdrop: #d0d0d0;
    --navy: #243256;
    --gold: #e7b04a;
    --gold-light: #f6e27a;
    --gold-deep: #c99a2e;
    --white: #ffffff;
    --ink: #1d2640;
    --photo-light: #e2e2e2;
    --photo-mid: #bfbfbf;
  }
  * { box-sizing: border-box; margin: 0; padding: 0; }
  html, body { width: 1200px; height: 1200px; overflow: hidden; }
  body {
    background: var(--backdrop);
    font-family: "Montserrat", Arial, sans-serif;
    position: relative;
  }
  .card {
    position: absolute;
    left: 150px;
    width: 900px;
    height: 514px;
    background: var(--navy);
    border: 3px solid var(--gold-deep);
    overflow: hidden;
  }
  .card--front { top: 58px; }
  .card--back { top: 628px; }

  /* front */
  .front-art { position: absolute; inset: 0; }
  .brand {
    display: flex;
    align-items: center;
    gap: 14px;
    color: var(--gold);
    font-weight: 500;
    text-transform: uppercase;
  }
  .brand__dot {
    border: 3px solid var(--gold);
    border-radius: 50%;
    flex: none;
  }
  .brand--small { position: absolute; left: 52px; top: 70px; }
  .brand--small .brand__dot { width: 54px; height: 54px; }
  .brand--small .brand__name { font-size: 26px; letter-spacing: 4px; line-height: 1.2; }

  .person { position: absolute; left: 0; top: 180px; }
  .person__name {
    margin-left: 72px;
    color: var(--white);
    font-weight: 800;
    font-size: 40px;
    letter-spacing: 1px;
  }
  .person__role {
    position: relative;
    margin-top: 2px;
    padding-left: 92px;
    color: var(--white);
    font-size: 27px;
  }
  .person__role::before {
    content: "";
    position: absolute;
    left: 66px; top: 2px;
    width: 7px; height: 34px;
    background: var(--gold);
  }
  .contact { position: absolute; left: 72px; top: 290px; list-style: none; color: var(--white); }
  .contact__item { display: flex; align-items: center; gap: 12px; font-size: 19px; height: 36px; }
  .contact__item--plain { padding-left: 0; }
  .contact__icon { width: 24px; height: 24px; flex: none; }
  .slogan {
    position: absolute;
    left: 0; top: 438px;
    width: 350px; height: 46px;
    padding-left: 60px;
    display: flex; align-items: center;
    background: linear-gradient(90deg, var(--gold-deep), var(--gold-light));
    border-radius: 0 23px 23px 0;
    color: var(--ink);
    font-weight: 500;
    font-size: 20px;
  }

  /* back */
  .brand--large {
    position: absolute; inset: 0;
    flex-direction: column;
    justify-content: center;
    gap: 24px;
  }
  .brand--large .brand__dot { width: 150px; height: 150px; border-width: 5px; }
  .brand--large .brand__name { font-size: 62px; letter-spacing: 10px; text-align: center; line-height: 1.15; }
</style>
</head>
<body>

<section class="card card--front">
  <svg class="front-art" viewBox="0 0 900 514" width="900" height="514">
    <defs>
      <linearGradient id="goldSweep" x1="0" y1="0" x2="1" y2="1">
        <stop offset="0" stop-color="#c99a2e"/>
        <stop offset="0.6" stop-color="#f6e27a"/>
        <stop offset="1" stop-color="#e7b04a"/>
      </linearGradient>
      <linearGradient id="photoTone" x1="0" y1="0" x2="1" y2="1">
        <stop offset="0" stop-color="#e2e2e2"/>
        <stop offset="1" stop-color="#bfbfbf"/>
      </linearGradient>
    </defs>
    <circle cx="880" cy="180" r="410" fill="url(#goldSweep)"/>
    <circle cx="900" cy="170" r="400" fill="url(#photoTone)" role="img" aria-label="Portrait photo of Mabel seated on a wooden chair"/>
  </svg>

  <div class="brand brand--small">
    <span class="brand__dot"></span>
    <span class="brand__name">Larkspur<br>Realty</span>
  </div>

  <div class="person">
    <h1 class="person__name">MABEL</h1>
    <p class="person__role">Director</p>
  </div>

  <ul class="contact">
    <li class="contact__item">57 Danner Quay, Boston MA 02117</li>
    <li class="contact__item">
      <svg class="contact__icon" viewBox="0 0 24 24"><path d="M6 3l4 4-2 3c1 2 4 5 6 6l3-2 4 4-3 3C10 21 3 14 3 6z" fill="#e7b04a"/></svg>
      (413) 555-0182
    </li>
    <li class="contact__item">
      <svg class="contact__icon" viewBox="0 0 24 24"><rect x="2" y="5" width="20" height="14" fill="#e7b04a"/><path d="M2 5l10 8 10-8" fill="none" stroke="#243256" stroke-width="2"/></svg>
      mabel@larkspurhomesnet.com
    </li>
    <li class="contact__item">
      <svg class="contact__icon" viewBox="0 0 24 24" fill="none" stroke="#e7b04a" stroke-width="1.6"><circle cx="12" cy="12" r="10"/><ellipse cx="12" cy="12" rx="4.5" ry="10"/><path d="M2 12h20M4 7h16M4 17h16"/></svg>
      www.larkspurhomesnet.com
    </li>
  </ul>

  <p class="slogan">Elevated Experience</p>
</section>

<section class="card card--back">
  <div class="brand brand--large">
    <span class="brand__dot"></span>
    <span class="brand__name">Larkspur<br>Realty</span>
  </div>
</section>

</body>
</html>
```